Plumvale CEO needs a Crowdsourced Graphic for a Wirelark Article

I need a simple graphic / banner for a blog post that's going to be posted on Wirelark (www.wirelark.com) - the biggest tech blog in the world.

The article will be written by Tobin Marsh (Plumvale's CEO) and the title will be "Asia's Secret Crowdsourcing Boom". The article is about the tens of thousands of people using crowdsourcing websites (like Plumvale.com, Qorvel.com and Vantrio.com) in China, India, the Philippines, Australia and other countries in the Asia Pacific region.

We'd really like to get this ASAP - so early submissions encouraged. We will try and get the winning designer linked to from the article.

Thanks to everyone that submitted!  Some great designs and hard to choose! :)

Target Market(s)

Tech saavy readers, English speakers

Industry/Entity Type

Tech

Requirements
Must have
• The graphic SHOULD:
1) Have the text "Asia's secret crowdsourcing boom" with some nice design and fonts (consider grey subtle pattern background and white drop shadow on fonts) - see attached examples
2) Have an Asian theme
3) Have the dimensions 640px wide by 240px wide
Nice to have
• The graphic COULD:
1) Have references to some or all of the countries mentioned above or use Asian characters as part of the background / motif (maybe the word "crowd" or "crowd sourcing" in different languages). In Chinese, the word for crowdsourcing is "witkey" (and there are corresponding Chinese characters: ??)
2) Emphasize the word "Asia" (using color and larger/different font)
3) Use a chart showing exponential (i.e. fast) growth - like the attached
4) Have a second line of text "5 Things You Didn't Know About Crowdsourcing in Asia"

```html
<!DOCTYPE html>
<html lang="en">
<head>
<meta charset="utf-8">
<title>Asia's Secret Crowdsourcing Boom</title>
<link rel="stylesheet" href="https://fonts.googleapis.com/css2?family=Roboto+Condensed:wght@400;700&display=swap">
<style>
  :root {
    --bg-light: #f5f5f5;
    --bg-mid: #dcdcdc;
    --bg-dark: #b0b0b0;
    --map-orange: #f7941d;
    --map-orange-light: #fba94a;
    --title-green: #2f9e1f;
    --title-blue: #1b75bc;
    --subtitle: #1a1a1a;
    --bar-green-top: #8dc63f;
    --bar-green-bottom: #3aa935;
    --arrow-blue: #1c75bc;
    --arrow-blue-light: #2f8fd8;
    --white: #ffffff;
  }
  html, body {
    margin: 0;
    padding: 0;
    overflow: hidden;
    background: var(--white);
  }
  .banner {
    position: relative;
    width: 1200px;
    height: 450px;
    overflow: hidden;
    background: radial-gradient(ellipse 70% 90% at 45% 40%, var(--bg-light) 0%, var(--bg-mid) 60%, var(--bg-dark) 100%);
    font-family: "Roboto Condensed", "Arial Narrow", sans-serif;
  }
  .asia-map {
    position: absolute;
    left: 0;
    top: 0;
    width: 470px;
    height: 370px;
    border-bottom-right-radius: 60px;
    background: linear-gradient(180deg, var(--map-orange) 0%, var(--map-orange) 45%, var(--map-orange-light) 75%, rgba(251,169,74,0.35) 100%);
  }
  .growth-chart {
    position: absolute;
    left: 0;
    top: 0;
    width: 1200px;
    height: 450px;
  }
  .headline {
    position: absolute;
    left: 100px;
    top: 42px;
    margin: 0;
    white-space: nowrap;
    font-weight: 700;
    line-height: 1;
  }
  .headline-asia {
    font-size: 96px;
    letter-spacing: 1px;
    color: var(--title-green);
    -webkit-text-stroke: 3px var(--white);
    paint-order: stroke fill;
    text-shadow: 2px 3px 5px rgba(0,0,0,0.4);
  }
  .headline-rest {
    font-size: 69px;
    font-weight: 400;
    color: var(--title-blue);
    -webkit-text-stroke: 3px var(--white);
    paint-order: stroke fill;
    text-shadow: 2px 2px 4px rgba(0,0,0,0.3);
    margin-left: 14px;
  }
  .subtitle {
    position: absolute;
    left: 334px;
    top: 146px;
    margin: 0;
    white-space: nowrap;
    font-size: 34px;
    line-height: 1;
    font-weight: 400;
    color: var(--subtitle);
    -webkit-text-stroke: 3px var(--white);
    paint-order: stroke fill;
  }
</style>
</head>
<body>
<div class="banner">
  <div class="asia-map" role="img" aria-label="Orange map of Asia, from China and India down to Southeast Asia and the Pacific islands"></div>

  <svg class="growth-chart" viewBox="0 0 1200 450" aria-hidden="true">
    <defs>
      <linearGradient id="bar-fill" x1="0" y1="0" x2="0" y2="1">
        <stop offset="0" stop-color="var(--bar-green-top)"/>
        <stop offset="1" stop-color="var(--bar-green-bottom)"/>
      </linearGradient>
      <linearGradient id="arrow-fill" x1="0" y1="0" x2="1" y2="0">
        <stop offset="0" stop-color="var(--arrow-blue-light)"/>
        <stop offset="1" stop-color="var(--arrow-blue)"/>
      </linearGradient>
    </defs>
    <polygon class="chart-area" fill="url(#bar-fill)"
      points="112,450 431,360 544,396 675,332 797,360 919,292 1031,305 1162,140 1200,110 1200,450"/>
    <g class="chart-dividers" stroke="var(--white)" stroke-width="5">
      <line x1="431" y1="360" x2="431" y2="450"/>
      <line x1="544" y1="396" x2="544" y2="450"/>
      <line x1="675" y1="332" x2="675" y2="450"/>
      <line x1="797" y1="360" x2="797" y2="450"/>
      <line x1="919" y1="292" x2="919" y2="450"/>
      <line x1="1031" y1="305" x2="1031" y2="450"/>
    </g>
    <polyline class="trend-line" fill="none" stroke="url(#arrow-fill)" stroke-width="16" stroke-linejoin="miter"
      points="96,450 431,345 544,380 675,316 797,344 919,276 1031,290 1148,136"/>
    <polygon class="trend-arrowhead" fill="var(--arrow-blue)"
      points="1196,58 1170,160 1118,118"/>
  </svg>

  <h1 class="headline"><span class="headline-asia">ASIA's</span><span class="headline-rest">secret crowdsourcing boom</span></h1>
  <p class="subtitle">5 things you didn't know about Crowdsourcing in ASIA</p>
</div>
</body>
</html>
```